Tarn Ridge Distillery - Velvet Hollow Label

We are Tarn Ridge Distillery, a family owned and operated New Zealand distillery redefining what quality means. We specialize in unique spirits handcrafted from the purest homegrown ingredients. With a family history of decades of distilling we’re staunchly dedicated to quality over quantity.
Its time to revamp our Velvet Hollow label. Velvet Hollow are fruit soaked in brandy, this delicious concoction is beautiful over ice cream or in cocktails. Its punchy on flavor and alcohol, sitting at 15% alcohol. Its a really popular product and needs a label to match. This is a dessert topping with attitude so we are after a bold label that reflects this, the liquid is dark purple/red with whole fruit still in it.

Since the liquid is red/purple, the label will need to match color wise. Possibly white and with gold or copper metallic highlights - we have found this is good for shelf appeal. But there is heaps of room for creative expression here, basically, the label needs to be bold and visible on a liquor store shelf from a distance. The jar is very beautiful too which will help with this.

I have attached files of the current label (that we don't like) with its measurements, the jar we are using and a bunch of different files containing our logo and our tag line "Born of the Southern Ranges"
We have two flavors of the Velvet Hollow. One is Boysenberry and the other is Morello Cherry.
The copy on the attached label is incorrect, I have rewritten what needs to be included below:
Name: Velvet Hollow
Flavour: Boysenberry OR Morello Cherry
Country of Origin : Born of the Southern Ranges
Alcohol: 30% ABV
Size: 300mL
Barcode: space for the image and number
Website: www.tarnridgedistillery.example.nz
Produced By: Produced By Tarn Ridge Distillery, 58 Corrowin Road 7342 Pellow Flats New Zealand
Ingredients: Boysenberries OR Morello Cherries 60%, Sugar 25%, Honey Brandy 15%
Per Serving breakdown: Please allow space for serving breakdown
Serving Suggestion: 10 Standard Drinks, Average Serving 30mL
Description: A luxurious Adult Topping made by immersing juicy local Boysenberries OR Morello Cherries in decadent Honey Brandy. A intense fruit topping that is perfect drizzled over ice cream, cakes or in cocktails. (Description copy can be rewritten)
Check out our website for more information about us www.tarnridgedistillery.example.nz

Target Market(s)

Adults, 18+

Requirements
Must have
• Name: Velvet Hollow
Alcohol: 30% ABV
Size: 300mL
Nice to have
• Our company font is Rubik Regular or Roboto for text, using another font is fine though if it suits the product better.
A label that has some cut outs so that you can see the contents of the jar could work quite well.
Should not have
• I don't think photo of a actual berry would work well with this label, I would prefer a illustrated picture or something like that.

```html
<!DOCTYPE html>
<html lang="en">
<head>
<meta charset="utf-8">
<title>Velvet Hollow – Boysenberry Label</title>
<link rel="stylesheet" href="https://fonts.googleapis.com/css2?family=Limelight&family=Rubik:wght@300;400;700&display=swap">
<style>
  :root {
    --page: #f4f2f0;
    --paper: #fbfaf9;
    --ink: #1d1a1b;
    --copper: #b06a45;
    --copper-light: #d8a27f;
    --copper-dark: #7c3f22;
    --sketch: #c9c6c6;
    --blush: #f1e3db;
  }
  * { margin: 0; padding: 0; box-sizing: border-box; }
  html, body { width: 801px; height: 1200px; overflow: hidden; background: var(--page); }
  .canvas { position: relative; width: 801px; height: 1200px; }

  .label {
    position: absolute; left: 50px; top: 200px; width: 701px; height: 800px;
    background: var(--paper); overflow: hidden;
    font-family: "Rubik", sans-serif; color: var(--ink);
  }
  .copper-band {
    position: absolute; left: 0; width: 100%; height: 22px;
    background: linear-gradient(180deg, var(--copper-light), var(--copper) 45%, var(--copper-dark));
  }
  .copper-band.top { top: 0; }
  .copper-band.bottom { bottom: 0; }

  .leaf-art {
    position: absolute; top: 22px; left: 0; width: 100%; height: 300px;
    background: radial-gradient(ellipse at 20% 30%, var(--blush), transparent 55%),
                radial-gradient(ellipse at 85% 35%, var(--blush), transparent 55%);
    opacity: .8;
  }
  .berry-art {
    position: absolute; left: 0; bottom: 22px; width: 100%; height: 320px;
    background: radial-gradient(ellipse at 25% 75%, var(--sketch), transparent 60%),
                radial-gradient(ellipse at 95% 40%, var(--sketch), transparent 45%),
                radial-gradient(ellipse at 5% 30%, var(--sketch), transparent 40%);
    opacity: .55;
  }

  .maker {
    position: absolute; top: 100px; left: 0; width: 100%;
    display: flex; justify-content: center; align-items: center; gap: 14px;
    font-weight: 700; font-size: 21px; letter-spacing: 6px; text-transform: uppercase;
  }
  .maker-dot { width: 14px; height: 14px; border-radius: 50%; background: var(--ink); }

  .product-name { position: absolute; top: 262px; left: 30px; width: 641px; height: 110px; }
  .product-name text { font-family: "Limelight", serif; font-size: 92px; fill: var(--ink); }

  .flavour {
    position: absolute; top: 424px; left: 0; width: 100%; text-align: center;
    font-weight: 700; font-size: 27px; letter-spacing: 11px; text-transform: uppercase;
  }
  .volume {
    position: absolute; top: 532px; left: 0; width: 100%; text-align: center;
    font-weight: 300; font-size: 23px; letter-spacing: 5px;
  }
  .origin-seal { position: absolute; left: 500px; top: 580px; width: 150px; height: 150px; }
  .origin-seal text { font-family: "Rubik", sans-serif; font-size: 13.5px; font-weight: 400; letter-spacing: 2.5px; fill: var(--ink); text-transform: uppercase; }
</style>
</head>
<body>
<main class="canvas">
  <section class="label">
    <div class="copper-band top"></div>
    <div class="leaf-art" role="img" aria-label="Faint line drawing of boysenberry leaves and fruit"></div>
    <div class="berry-art" role="img" aria-label="Line drawing of boysenberries on their stems"></div>

    <div class="maker"><span class="maker-dot"></span>Tarn Ridge Distillery</div>

    <svg class="product-name" viewBox="0 0 641 110" aria-label="Velvet Hollow">
      <text x="320" y="88" text-anchor="middle" textLength="630" lengthAdjust="spacingAndGlyphs">VELVET HOLLOW</text>
    </svg>

    <p class="flavour">Boysenberry</p>
    <p class="volume">30% ABV | 300ML</p>

    <svg class="origin-seal" viewBox="0 0 150 150">
      <circle cx="75" cy="75" r="70" fill="none" stroke="var(--ink)" stroke-width="2.5"/>
      <defs>
        <path id="seal-ring" d="M75,75 m-52,0 a52,52 0 1,1 104,0 a52,52 0 1,1 -104,0"/>
      </defs>
      <text><textPath href="#seal-ring" startOffset="2%">Born of the Southern Ranges ·</textPath></text>
    </svg>

    <div class="copper-band bottom"></div>
  </section>
</main>
</body>
</html>
```